Stationery Design Project

We need a stationary design for a well-known architect in Guadalajara, Mexico. This architect specializes in very luxurious homes and commercial developments. His clients are very sophisticated, so the letterhead should be equally sophisticated. References to mythology, etc. might be a plus. The letterhead may be embossed and will be printed on a heavy-weight linen. His homes and developments are very luxurious but not necessarily ultra-modern in their aesthetic.
Target Market(s)
High end developers and luxury home buyers
Industry/Entity Type
Architect
Look and feel

```html
<!DOCTYPE html>
<html lang="es">
<head>
<meta charset="utf-8">
<title>Arq. Tomás Vidaurri — Papelería</title>
<link rel="stylesheet" href="https://fonts.googleapis.com/css2?family=Marcellus&display=swap">
<style>
  :root {
    --navy: #0f3a6e;
    --navy-dark: #0b2f5c;
    --steel: #4d74a0;
    --paper: #ffffff;
    --paper-shade: #eeeeef;
    --ink: #555a60;
    --ink-soft: #8a8f96;
    --backdrop: #5f5f61;
    --window: #f3f3f5;
  }
  * { box-sizing: border-box; margin: 0; padding: 0; }
  html, body { width: 1200px; height: 900px; overflow: hidden; }
  body {
    background: var(--backdrop);
    font-family: "Marcellus", "Optima", serif;
    color: var(--ink);
    position: relative;
  }
  .sheet { position: absolute; background: var(--paper); box-shadow: 0 6px 18px rgba(0,0,0,.35); overflow: hidden; }
  .wordmark { font-variant: small-caps; color: var(--navy); letter-spacing: .06em; white-space: nowrap; }
  .band-art { position: absolute; top: 0; left: 0; display: block; }

  /* Letterhead */
  .letterhead { left: 40px; top: 110px; width: 480px; height: 679px;
    background: linear-gradient(180deg, var(--paper) 60%, var(--paper-shade)); }
  .letterhead .wordmark { position: absolute; left: 30px; top: 26px; font-size: 17px; }
  .letter-body { position: absolute; left: 60px; top: 96px; width: 370px; font-size: 7.6px; line-height: 1.55; color: var(--ink); }
  .salutation { color: var(--navy); font-size: 9px; margin-bottom: 10px; }
  .letter-body p { margin-bottom: 10px; text-align: left; }
  .closing { position: absolute; left: 60px; top: 470px; font-size: 8px; }
  .signature { width: 90px; height: 50px; margin: 8px 0 6px; background: linear-gradient(90deg, #f1f2f4, #e4e6ea); border-radius: 3px; }
  .signer { color: var(--navy); font-size: 9px; }
  .signer-title { font-size: 8px; }
  .letterhead .address { position: absolute; left: 60px; bottom: 28px; }
  .address { font-size: 7px; line-height: 1.45; color: var(--ink-soft); }
  .address .navy { color: var(--navy); }
  .corner { position: absolute; left: 0; bottom: 0; }

  /* Envelope */
  .envelope { left: 540px; top: 110px; width: 620px; height: 310px;
    background: linear-gradient(160deg, var(--paper) 55%, var(--paper-shade)); }
  .envelope .wordmark { position: absolute; left: 36px; top: 54px; font-size: 18px; }
  .envelope-window { position: absolute; right: 40px; top: 110px; width: 210px; height: 108px;
    border: 1px solid #9a9ca0; border-radius: 10px; background: var(--window); }
  .envelope .address { position: absolute; left: 40px; bottom: 30px; color: var(--navy); font-weight: 400; font-size: 7.5px; }

  /* Business cards */
  .card { width: 290px; height: 166px; top: 480px; }
  .card-front { left: 540px; }
  .card-front .wordmark { position: absolute; left: 22px; top: 66px; font-size: 15px; }
  .card-front .address { position: absolute; left: 24px; top: 96px; }
  .card-back { left: 870px; background: var(--navy-dark); }
  .card-back .wordmark { position: absolute; left: 50%; top: 74px; transform: translateX(-50%); color: var(--paper); font-size: 13px; }
</style>
</head>
<body>

  <section class="sheet letterhead" aria-label="Hoja membretada">
    <svg class="band-art" width="480" height="80" viewBox="0 0 480 80" aria-hidden="true">
      <rect x="0" y="50" width="188" height="9" fill="var(--navy)"/>
      <polygon points="196,59 226,22 480,22 480,0 245,0 196,59" fill="var(--navy)" opacity="0"/>
      <polygon points="190,48 214,18 480,18 480,30 224,30 204,48" fill="var(--navy)"/>
    </svg>
    <div class="wordmark">Arq. Tomás Vidaurri</div>

    <div class="letter-body">
      <div class="salutation">Dear Mr. John Doe</div>
      <p>Lorem ipsum dolor sit amet, consectetur adipiscing elit. Duis elit nunc, iaculis vitae dictum non, adipiscing a ante. Donec quis purus tellus. Nunc sed lacus sit amet lectus mattis rhoncus aliquet id elit. Nam quam et nisl bibendum consequat et quis velit. Donec id nisi vel orci elementum gravida id eget eu libero urna, sit amet volutpat neque. Donec arcu lacus, interdum sit amet iaculis vitae, ipsum. Pellentesque eu diam vel dolor suscipit interdum tincidunt facilisis lacus.</p>
      <p>Nunc augue, laoreet non fringilla sit amet, congue eget mauris. Pellentesque id metus elit. Mortis leo nec est tristique quis tempor risus venenatis. Maecenas congue nibh sit amet nisi egestas tortor molestie. Nullam commodo arcu ac tellus cursus id rutrum urna tempor. Mauris diam, eu fringilla nisl. Aliquam varius urna non urna condimentum quis gravida odio suscipit. Quis arcu felis. Suspendisse interdum feugiat odio, luctus rutrum velit pellentesque et. Adipiscing scelerisque magna.</p>
      <p>Nunc nibh nibh, luctus quis tempus id, pretium tincidunt neque. Nam pulvinar, augue vitae tristique nisi sem tristique purus, eget suscipit dolor diam sed nisl. Lorem ipsum dolor sit amet, adipiscing elit. Cras consectetur accumsan commodo. Nunc dapibus sem quis sapien pellentesque sapien fringilla. Nullam id arcu quis orci suscipit porta non vitae purus. Tristique ligula non metus auctor at laoreet ipsum tincidunt. Suspendisse eleifend. Sed dignissim pulvinar diam non tempor. Aenean interdum eleifend arcu. Cras ac ornare purus. Vestibulum nisl velit, tincidunt nec fringilla commodo.</p>
      <p>Ullamcorper velit. Aliquam nec dolor aliquet justo porttitor molestie. Etiam ullamcorper. Cras ipsum sem, scelerisque ullamcorper dapibus sed, egestas neque. In in tortor suscipit diam sagittis mattis. Nulla tincidunt molestie in.</p>
    </div>

    <div class="closing">
      <div>Sincerely</div>
      <div class="signature" role="img" aria-label="Firma manuscrita del arquitecto"></div>
      <div class="signer">Lorem Ipsum</div>
      <div class="signer-title">Senior Architect</div>
    </div>

    <div class="address">
      <div class="navy">Calle de los Olivos 1450</div>
      <div class="navy">Colonia Jardines del Sol C.P. 45050</div>
      <div>Zapopan, Jalisco - México</div>
      <div>Tel: (52) 33 1234 5678</div>
    </div>
    <svg class="corner" width="34" height="34" viewBox="0 0 34 34" aria-hidden="true">
      <polygon points="0,0 22,0 0,34" fill="var(--navy)" transform="translate(0,0)"/>
    </svg>
  </section>

  <section class="sheet envelope" aria-label="Sobre">
    <svg class="band-art" width="620" height="100" viewBox="0 0 620 100" aria-hidden="true">
      <defs>
        <linearGradient id="envelope-band" x1="0" x2="1" y1="0" y2="0">
          <stop offset="0" stop-color="var(--navy)"/>
          <stop offset="1" stop-color="var(--steel)"/>
        </linearGradient>
      </defs>
      <rect x="0" y="78" width="212" height="10" fill="var(--navy)"/>
      <polygon points="222,88 256,50 620,50 620,0 600,0 600,36 246,36 212,78 222,78" fill="url(#envelope-band)" opacity="0"/>
      <polygon points="220,76 244,46 620,46 620,62 254,62 232,88 220,88" fill="url(#envelope-band)"/>
    </svg>
    <div class="wordmark">Arq. Tomás Vidaurri</div>
    <div class="envelope-window"></div>
    <div class="address">
      <div>Calle de los Olivos 1450</div>
      <div>Colonia Jardines del Sol C.P. 45050</div>
      <div>Zapopan, Jalisco - México</div>
    </div>
  </section>

  <section class="sheet card card-front" aria-label="Tarjeta de presentación, frente">
    <svg class="band-art" width="290" height="90" viewBox="0 0 290 90" aria-hidden="true">
      <rect x="0" y="86" width="150" height="4" fill="var(--navy)" opacity="0"/>
      <polygon points="148,40 170,14 290,14 290,40" fill="var(--steel)"/>
    </svg>
    <div class="wordmark">Arq. Tomás Vidaurri</div>
    <div class="address">
      <div>Calle de los Olivos 1450</div>
      <div>Colonia Jardines del Sol C.P. 45050</div>
      <div>Zapopan, Jalisco - México</div>
      <div>Tel: (52) 33 1234 5678</div>
    </div>
  </section>

  <section class="sheet card card-back" aria-label="Tarjeta de presentación, reverso">
    <svg class="band-art" width="290" height="166" viewBox="0 0 290 166" aria-hidden="true">
      <polygon points="0,58 290,58 290,112 0,112" fill="var(--paper)" opacity="0"/>
      <polygon points="0,96 60,96 76,76 290,76 290,98 88,98 72,118 0,118" fill="var(--paper)"/>
    </svg>
    <div class="wordmark">Tomás Vidaurri</div>
  </section>

</body>
</html>
```